Website Homepage Design for New Cosmetic Line

Design the Homepage for the website based on a provided Wireframe. Assets have been be provided for the design, with the expectation that the designer will provide the creative flair. Along with the homepage design, a list of site fonts and colours will also be needed for internal pages (but no internal page designs required. )
Layout/wireframe is here: http://verano-plumcosmetics.com/layout/ (and also attached in files as PNG and PDF)
No need to follow the Layout exactly as far as spacing and font go, just make sure all elements are on the page, and look amazing!
My Client gave these sites for comparable in the industry:
https://www.quorvabeauty.com/
https://www.marisoltenderwoodglow.com/ (does not like video in header though)

Moving Down the Wireframe:
Header Logo - Use the Text only from the logo, not the Circle at the top here
Navigation - Copy these items
Hero Image: Use the image stated. Feel free to add some creativity over it, make sure that the lips and product are still visible, and also that the Text that is being overlaid can be easily read
Arm Swatch and Lip Swatches, make them pop!
Featured Products, 2 of the images are in RAW from the photographer - you may want to convert them to jpg. Feel free to adjust if needed, for sizing and brightness. If you want to crop the images from the backgrounds, you could do that too to allow for more consistency.
Reviews show the needed content as well.

Footer speaks for itself - use the Full Round Logo here.

All Assets are here: https://files.stashbarn.net/folders/8kQwLmZ2xR4tYp9VnHc3JdE6sUb7aGo?usp=sharing

The main assets are also attached in a zip file, but there are more in the above shared link for additional creativity/resources

• Unique and Beautiful Design
Clear Layout
Follow Best Practices in Design layout for development (eg based on 12 grid)
Please Use Google Fonts

```html
<!DOCTYPE html>
<html lang="en">
<head>
<meta charset="utf-8">
<title>Verano-Plum Cosmetics — Home</title>
<link rel="stylesheet" href="https://fonts.googleapis.com/css2?family=Poppins:wght@300;400;500;600;700&family=Josefin+Sans:wght@200;300;400&family=Great+Vibes&family=Libre+Baskerville&display=swap">
<style>
  :root {
    --ink: #111111;
    --text: #333333;
    --muted: #777777;
    --pink: #d9638f;
    --blush: #fde6e8;
    --rose-btn: #f28c98;
    --band: #f4f4f4;
    --line: #e6e6e6;
    --white: #ffffff;
    --link-pink: #f07a8a;
  }
  * { box-sizing: border-box; margin: 0; padding: 0; }
  html, body { width: 1200px; height: 2844px; overflow: hidden; background: var(--white); }
  body { font-family: "Poppins", sans-serif; color: var(--text); }
  .page { position: relative; width: 1200px; height: 2844px; overflow: hidden; }
  .abs { position: absolute; }

  /* Header */
  .brand { left: 0; width: 1200px; top: 18px; text-align: center; font-family: "Josefin Sans", sans-serif; font-weight: 200; font-size: 56px; color: var(--ink); letter-spacing: -1px; }
  .main-nav { left: 234px; top: 111px; width: 732px; height: 35px; background: var(--ink); display: flex; justify-content: center; align-items: center; }
  .main-nav a { color: var(--white); text-decoration: none; font-size: 9px; font-weight: 600; letter-spacing: 1px; padding: 0 20px; border-right: 1px solid #666; line-height: 12px; }
  .main-nav a:last-child { border-right: 0; }

  /* Hero */
  .hero { left: 234px; top: 164px; width: 732px; height: 297px; overflow: hidden; }
  .hero-photo { position: absolute; inset: 0; background: linear-gradient(120deg, #2a2422 0%, #5b4038 30%, #b6577c 55%, #6c6460 80%); }
  .hero svg.panel { position: absolute; inset: 0; }
  .hero-copy { position: absolute; left: 450px; width: 282px; top: 44px; text-align: center; color: var(--white); }
  .hero-script { font-family: "Great Vibes", cursive; font-size: 34px; line-height: 40px; }
  .hero-title { font-family: "Josefin Sans", sans-serif; font-weight: 300; font-size: 28px; letter-spacing: 3px; line-height: 31px; }
  .hero-sub { font-family: "Josefin Sans", sans-serif; font-weight: 300; font-size: 19px; letter-spacing: 2px; margin-top: 4px; }
  .btn { display: inline-block; background: var(--ink); color: var(--white); font-size: 10px; letter-spacing: 1px; text-align: center; text-decoration: none; }
  .hero-btn { margin-top: 14px; width: 112px; height: 34px; line-height: 34px; }
  .hero-dots { position: absolute; left: 558px; top: 259px; display: flex; gap: 5px; }
  .hero-dots span { width: 12px; height: 12px; border: 2px solid var(--white); border-radius: 50%; }
  .hero-dots span.active { background: radial-gradient(circle, var(--white) 35%, transparent 40%); }

  /* Section headings */
  .section-title { left: 0; width: 1200px; text-align: center; font-size: 17px; font-weight: 500; letter-spacing: 2.5px; color: var(--ink); }

  .mission-text { left: 234px; width: 732px; top: 592px; text-align: center; font-size: 12.5px; line-height: 21px; color: var(--text); }
  .mission-tag { left: 0; width: 1200px; top: 654px; text-align: center; font-size: 12.5px; }

  /* Swatches */
  .arm-swatch { left: 234px; top: 721px; width: 732px; height: 343px; background: linear-gradient(180deg, #8a6a5c 0%, #a17b69 35%, #c49a86 50%, #9c7663 70%, #7b5d50 100%); }
  .swatch-frame { position: absolute; border: 3px solid var(--white); }
  .arm-swatch .swatch-frame { left: 23px; top: 23px; right: 23px; bottom: 23px; }
  .arm-label { position: absolute; right: 50px; bottom: 52px; font-family: "Libre Baskerville", serif; font-size: 31px; color: var(--ink); }
  .lip-row { left: 234px; top: 1085px; width: 732px; height: 219px; display: flex; }
  .lip-swatch { position: relative; flex: 1; }
  .lip-swatch:nth-child(1) { background: linear-gradient(135deg, #e8556a, #9a3b3b 50%, #ef6070); }
  .lip-swatch:nth-child(2) { background: linear-gradient(135deg, #2b3a44, #d04a6a 50%, #3a2e3c); }
  .lip-swatch:nth-child(3) { background: linear-gradient(135deg, #f1a4a4, #e8404f 50%, #f0c6c0); }
  .lip-swatch .swatch-frame { left: 17px; right: 17px; top: 15px; bottom: 15px; border-width: 2px; }
  .lip-label { position: absolute; left: 0; right: 0; top: 96px; text-align: center; font-family: "Libre Baskerville", serif; font-size: 18px; color: var(--white); text-shadow: 0 1px 3px rgba(0,0,0,.4); }

  /* Featured */
  .featured-band { left: 0; top: 1366px; width: 1200px; height: 552px; background: var(--band); }
  .product { width: 250px; text-align: center; }
  .product-visual { width: 160px; height: 170px; margin: 0 auto; border-radius: 8px; }
  .product-name { margin-top: 30px; font-size: 15px; font-weight: 600; color: var(--ink); line-height: 18px; height: 40px; display: flex; align-items: flex-end; justify-content: center; }
  .product-btn { margin-top: 8px; width: 113px; height: 34px; line-height: 34px; }

  /* Reviews */
  .review-card { top: 2066px; width: 232px; height: 245px; background: var(--white); border: 1px solid var(--line); padding: 19px 19px; }
  .review-head { display: flex; align-items: center; gap: 12px; }
  .avatar { width: 48px; height: 48px; border-radius: 50%; background: linear-gradient(135deg, #c7a08e, #6b4a3c); }
  .review-type { font-size: 10px; font-weight: 700; color: var(--ink); }
  .stars { display: flex; gap: 1px; margin-top: 2px; }
  .review-body { margin-top: 16px; font-size: 8.6px; line-height: 15px; color: var(--muted); }
  .slider-dots { left: 565px; top: 2352px; display: flex; gap: 4px; }
  .slider-dots span { width: 22px; height: 2px; background: #ccc; }
  .slider-dots span.active { background: var(--ink); }

  /* Newsletter */
  .news-band { left: 0; top: 2408px; width: 1200px; height: 240px; background: var(--band); }
  .news-art { left: 0; top: 2416px; width: 237px; height: 222px; background: linear-gradient(135deg, #f7e3ec 0%, #efc9dc 45%, #dfe8f1 100%); }
  .news-title { left: 0; width: 1200px; top: 2474px; text-align: center; font-size: 18px; font-weight: 500; letter-spacing: 2px; color: var(--ink); }
  .news-label { left: 260px; top: 2548px; font-size: 17px; font-weight: 600; color: var(--ink); }
  .news-input { left: 532px; top: 2539px; width: 290px; height: 40px; background: var(--white); border: 1px solid var(--line); font-size: 11px; color: var(--muted); padding-left: 10px; line-height: 38px; }
  .news-btn { left: 822px; top: 2539px; width: 111px; height: 40px; background: var(--rose-btn); color: var(--white); font-size: 11px; font-weight: 600; text-align: center; line-height: 40px; letter-spacing: .5px; }

  /* Footer */
  .footer-links { left: 235px; top: 2694px; font-size: 11.5px; line-height: 22px; color: var(--text); }
  .copyright { left: 235px; top: 2783px; font-size: 8.5px; color: var(--text); }
  .footer-seal { left: 545px; top: 2691px; width: 110px; height: 110px; border-radius: 50%; border: 2px dotted #999; display: flex; align-items: center; justify-content: center; }
  .footer-seal span { font-family: "Josefin Sans", sans-serif; font-weight: 300; font-size: 10px; color: var(--ink); }
  .footer-note { right: 234px; top: 2696px; text-align: right; font-size: 11.5px; line-height: 15px; color: var(--text); }
  .social { top: 2734px; width: 38px; height: 38px; border-radius: 50%; background: var(--ink); }
  .credit { right: 234px; top: 2783px; font-size: 8.5px; color: var(--text); }
  .credit a { color: var(--link-pink); text-decoration: none; }
</style>
</head>
<body>
<div class="page">

  <header>
    <div class="abs brand">Verano-Plum Cosmetics</div>
    <nav class="abs main-nav">
      <a href="#">PRODUCTS</a><a href="#">ABOUT US</a><a href="#">HOW TO'S</a><a href="#">BLOG</a><a href="#">CONNECT WITH US</a>
    </nav>
  </header>

  <section class="abs hero">
    <div class="hero-photo" role="img" aria-label="Close-up of lips wearing pink gloss beside a pink liquid lipstick tube"></div>
    <svg class="panel" width="732" height="297" viewBox="0 0 732 297">
      <polygon points="480,0 732,0 732,297 420,297" fill="#d9638f" opacity="0.92"/>
    </svg>
    <div class="hero-copy">
      <div class="hero-script">Look Gorgeous</div>
      <div class="hero-title">COSMETICS</div>
      <div class="hero-title">ACCESSORIES</div>
      <div class="hero-sub">Everything You Need</div>
      <a class="btn hero-btn" href="#">SHOP NOW</a>
    </div>
    <div class="hero-dots"><span class="active"></span><span></span><span></span></div>
  </section>

  <h2 class="abs section-title" style="top:534px;">OUR MISSION</h2>
  <p class="abs mission-text">Verano-Plum Cosmetics was created for inclusivity. An all-Canadian brand inspired by the cultural<br>mosaic we live in with colours unbound by to women of colour.</p>
  <p class="abs mission-tag">By us. For all.</p>

  <section class="abs arm-swatch" role="img" aria-label="Two arms showing lip colour swatches in plum, red, nude and berry">
    <div class="swatch-frame"></div>
    <div class="arm-label">ARM SWATCH</div>
  </section>

  <section class="abs lip-row">
    <div class="lip-swatch" role="img" aria-label="Collage of red lip palette swatches"><div class="swatch-frame"></div><div class="lip-label">LIP SWATCH 1</div></div>
    <div class="lip-swatch" role="img" aria-label="Collage of pink and berry lip palette swatches"><div class="swatch-frame"></div><div class="lip-label">LIP SWATCH 2</div></div>
    <div class="lip-swatch" role="img" aria-label="Collage of coral lip palette swatches"><div class="swatch-frame"></div><div class="lip-label">LIP SWATCH 3</div></div>
  </section>

  <div class="abs featured-band"></div>
  <h2 class="abs section-title" style="top:1448px;">FEATURED PRODUCTS</h2>

  <div class="abs product" style="left:225px; top:1555px;">
    <div class="product-visual" role="img" aria-label="Photo of a red liquid lipstick tube" style="background:linear-gradient(180deg,#f7e4e6 0%,#f3c9cc 55%,#e9a9ab 100%);"></div>
    <div class="product-name">Liquid Lipstick</div>
    <a class="btn product-btn" href="#">SHOP NOW</a>
  </div>

  <div class="abs product" style="left:475px; top:1555px;">
    <div class="product-visual" role="img" aria-label="Photo of an open warm lip palette" style="background:linear-gradient(180deg,#f7e4e6 0%,#efc2c0 55%,#e3a3a0 100%);"></div>
    <div class="product-name">Warm Lip Palette</div>
    <a class="btn product-btn" href="#">SHOP NOW</a>
  </div>

  <div class="abs product" style="left:725px; top:1555px;">
    <div class="product-visual" role="img" aria-label="Photo of an open sunset eye shadow palette" style="background:linear-gradient(180deg,#f7e4e6 0%,#f3cdb9 55%,#ebb195 100%);"></div>
    <div class="product-name">Eye Shadow Sunset<br>Palette</div>
    <a class="btn product-btn" href="#">SHOP NOW</a>
  </div>

  <h2 class="abs section-title" style="top:1996px;">REVIEWS</h2>

  <article class="abs review-card" style="left:234px;">
    <div class="review-head">
      <div class="avatar" role="img" aria-label="Reviewer portrait"></div>
      <div><div class="review-type">LIP GLOSS</div>
        <div class="stars"><svg width="58" height="11" viewBox="0 0 58 11" fill="#f5a623"><g id="s"><polygon points="5.5,0 7,3.8 11,4 8,6.6 9,10.6 5.5,8.4 2,10.6 3,6.6 0,4 4,3.8"/></g><use href="#s" x="11.7"/><use href="#s" x="23.4"/><use href="#s" x="35.1"/><use href="#s" x="46.8"/></svg></div></div>
    </div>
    <p class="review-body">This lipgloss is amazing, this shade i tried is called 'Velvetine'. 'Velvetine' is very moisturizing and easy to apply. A little goes a long way as i only needed two dabs of gloss. The gloss feels very smooth and has a nice smell. The gloss lasted a couple of hours before I needed to reapply. Over all I was very pleased with the lipgloss and I definitely try the other colours in the line. R.T.</p>
  </article>

  <article class="abs review-card" style="left:484px;">
    <div class="review-head">
      <div class="avatar" role="img" aria-label="Reviewer portrait"></div>
      <div><div class="review-type">LIP GLOSS</div>
        <div class="stars"><svg width="58" height="11" viewBox="0 0 58 11" fill="#f5a623"><use href="#s"/><use href="#s" x="11.7"/><use href="#s" x="23.4"/><use href="#s" x="35.1"/><use href="#s" x="46.8"/></svg></div></div>
    </div>
    <p class="review-body">Love this colour! The gloss goes on super easy and it barely feels like you're wearing anything on your lips at all. I hate the sticky feeling that some glosses leave but this one is awesome. I don't wear a lot of makeup so this is the perfect thing to just throw on when I'm in a rush and wanna glam up a bit. The gloss I chose is called 'SHINE BABE' and it definitely makes you feel that way. L.B.</p>
  </article>

  <article class="abs review-card" style="left:734px;">
    <div class="review-head">
      <div class="avatar" role="img" aria-label="Reviewer portrait"></div>
      <div><div class="review-type">LIP GLOSS</div>
        <div class="stars"><svg width="58" height="11" viewBox="0 0 58 11" fill="#f5a623"><use href="#s"/><use href="#s" x="11.7"/><use href="#s" x="23.4"/><use href="#s" x="35.1"/><use href="#s" x="46.8"/></svg></div></div>
    </div>
    <p class="review-body">Maplette is a beautiful, light everyday gloss. If you're looking for a quick grab-and-go, this is definitely it. Not sticky at all either. D.A.N.</p>
  </article>

  <div class="abs slider-dots"><span class="active"></span><span></span><span></span></div>

  <section>
    <div class="abs news-band"></div>
    <div class="abs news-art" role="img" aria-label="Watercolour illustration of an eye with pink splashes"></div>
    <h2 class="abs news-title">ALL CANADIAN - ALL INCLUSIVE</h2>
    <div class="abs news-label">Subscribe to our Newsletter</div>
    <div class="abs news-input">Enter Your Email</div>
    <div class="abs news-btn">SUBSCRIBE</div>
  </section>

  <footer>
    <div class="abs footer-links">About VPC<br>Blog<br>Sitemap</div>
    <div class="abs copyright">© 2020 Verano-Plum Cosmetics. All Rights Reserved.</div>
    <div class="abs footer-seal"><span>Verano-Plum Cosmetics</span></div>
    <div class="abs footer-note">Verano-Plum Cosmetics is a Vegan and<br>Cruelty-Free Brand</div>
    <div class="abs social" style="left:883px;" aria-label="Social profile"></div>
    <div class="abs social" style="left:928px;" aria-label="Social profile"></div>
    <div class="abs credit">Website Design by <a href="#">PixelwrenDigital.com</a></div>
  </footer>

</div>
</body>
</html>
```